Firm Stationery Design

I need a design for stationery, including: Stationery First Page, Stationery Second Sheet, Envelope, Mailing Label for Flat Envelopes, and Business Cards

```html
<!DOCTYPE html>
<html lang="en">
<head>
<meta charset="utf-8">
<title>Marlow Law LLC – Stationery</title>
<link href="https://fonts.googleapis.com/css2?family=Montserrat:wght@400;500;800&display=swap" rel="stylesheet">
<style>
  :root {
    --backdrop: #959495;
    --paper: #ffffff;
    --ink: #1b1b1d;
    --amber: #f5a01f;
    --amber-deep: #d98a12;
    --shadow: 0 6px 10px rgba(0,0,0,.28);
  }
  html, body { margin: 0; padding: 0; overflow: hidden; }
  body { width: 743px; height: 1200px; }
  .canvas {
    position: relative; width: 743px; height: 1200px; overflow: hidden;
    background: var(--backdrop);
    font-family: "Montserrat", sans-serif; color: var(--ink);
  }
  .sheet, .card, .envelope {
    position: absolute; background: var(--paper); box-shadow: var(--shadow); overflow: hidden;
  }
  .shapes { position: absolute; inset: 0; width: 100%; height: 100%; }
  .ink { fill: var(--ink); }
  .amber { fill: var(--amber); }

  .sheet { left: 48px; top: 61px; width: 490px; height: 692px; }
  .card { left: 435px; width: 266px; height: 156px; }
  .card--front { top: 217px; }
  .card--back { top: 396px; }
  .envelope { left: 42px; top: 800px; width: 659px; height: 328px; }

  /* firm name block */
  .firm {
    position: absolute; display: flex; flex-direction: column; align-items: center;
    transform: translateX(-50%); font-weight: 800; color: var(--ink); line-height: 1;
  }
  .firm__square { background: var(--amber); }
  .firm__name { letter-spacing: .01em; }
  .firm__suffix { letter-spacing: .55em; margin-right: -.55em; }

  .sheet .firm { left: 103px; top: 45px; }
  .sheet .firm__square { width: 48px; height: 48px; margin-bottom: 10px; }
  .sheet .firm__name { font-size: 29px; }
  .sheet .firm__suffix { font-size: 10px; margin-top: 8px; }

  .card--front .firm { left: 72px; top: 41px; }
  .card--front .firm__square { width: 28px; height: 28px; margin-bottom: 7px; }
  .card--front .firm__name { font-size: 16px; }
  .card--front .firm__suffix { font-size: 5.5px; margin-top: 5px; }

  .card--back .firm { left: 134px; top: 30px; }
  .card--back .firm__square { width: 38px; height: 38px; margin-bottom: 9px; }
  .card--back .firm__name { font-size: 21px; }
  .card--back .firm__suffix { font-size: 7px; margin-top: 7px; }

  .envelope .firm { left: 511px; top: 50px; }
  .envelope .firm__square { width: 54px; height: 54px; margin-bottom: 13px; }
  .envelope .firm__name { font-size: 31px; }
  .envelope .firm__suffix { font-size: 11px; margin-top: 10px; }

  /* contact lines */
  .contact { position: absolute; display: flex; align-items: center; white-space: nowrap; font-weight: 400; }
  .contact svg { flex: none; }
  .web { position: absolute; color: var(--amber); white-space: nowrap; font-weight: 400; transform: translateY(-50%); }

  .sheet .contact { left: 42px; font-size: 14.5px; gap: 8px; transform: translateY(-50%); }
  .sheet .contact svg { width: 9px; height: 10px; }
  .sheet .web { left: 316px; top: 664px; font-size: 14.5px; }

  .card-contacts {
    position: absolute; right: 23px; top: 57px; display: flex; flex-direction: column;
    align-items: flex-end; gap: 4px; font-size: 7.5px;
  }
  .card-contacts .contact { position: static; gap: 6px; }
  .card-contacts .contact svg { width: 5px; height: 6px; }
  .card-contacts .contact--web { color: var(--amber-deep); font-weight: 500; }

  .envelope .contact { left: 54px; font-size: 18.5px; gap: 10px; transform: translateY(-50%); }
  .envelope .contact svg { width: 11px; height: 13px; }
  .envelope .web { left: 439px; top: 293px; font-size: 18.5px; }
</style>
</head>
<body>
<div class="canvas">

  <!-- Letterhead -->
  <section class="sheet" aria-label="Letterhead">
    <svg class="shapes" viewBox="0 0 633 894" preserveAspectRatio="none" aria-hidden="true">
      <path class="ink" d="M0 871 L318 871 Q328 871 335 863 L357 840 Q363 834 372 834 L633 834 L633 894 L0 894 Z"/>
      <path class="amber" d="M0 847 H316 Q324 847 320 853 L315 860 Q312 864 305 864 H0 Z"/>
    </svg>
    <div class="firm">
      <span class="firm__square"></span>
      <span class="firm__name">MARLOW</span>
      <span class="firm__suffix">LAW LLC</span>
    </div>
    <div class="contact" style="top:606px">
      <svg viewBox="0 0 9 12"><rect x="1" y="0.7" width="7" height="10.6" rx="1.2" fill="none" stroke="currentColor" stroke-width="1.3"/><rect x="3.5" y="9" width="2" height="1" fill="currentColor"/></svg>
      <span>+39 000 5550142</span>
    </div>
    <div class="contact" style="top:632px">
      <svg viewBox="0 0 10 8"><rect width="10" height="8" rx="1" fill="currentColor"/><path d="M1 1.5 L5 4.5 L9 1.5" fill="none" stroke="#fff" stroke-width="1"/></svg>
      <span>office@marlowlaw.com</span>
    </div>
    <span class="web">www.marlowlaw.com</span>
  </section>

  <!-- Business card, front -->
  <section class="card card--front" aria-label="Business card front">
    <svg class="shapes" viewBox="0 0 344 202" preserveAspectRatio="none" aria-hidden="true">
      <path class="ink" d="M0 0 H344 V14 H172 Q165 14 160 19 L150 29 Q145 34 138 34 H0 Z"/>
      <path class="amber" d="M178 16 H344 V26 H171 L174 19 Q176 16 180 16 Z"/>
      <path class="amber" d="M0 181 H182 L204 160 H344 V171 H246 L226 193 H0 Z"/>
    </svg>
    <div class="firm">
      <span class="firm__square"></span>
      <span class="firm__name">MARLOW</span>
      <span class="firm__suffix">LAW LLC</span>
    </div>
    <div class="card-contacts">
      <div class="contact"><span>+39 000 5550142</span>
        <svg viewBox="0 0 9 12"><rect x="1" y="0.7" width="7" height="10.6" rx="1.2" fill="none" stroke="currentColor" stroke-width="1.4"/></svg></div>
      <div class="contact"><span>office@marlowlaw.com</span>
        <svg viewBox="0 0 10 8"><rect width="10" height="8" rx="1" fill="currentColor"/></svg></div>
      <div class="contact contact--web"><span>www.marlowlaw.com</span>
        <svg viewBox="0 0 10 10"><circle cx="5" cy="5" r="4.2" fill="none" stroke="var(--ink)" stroke-width="1.4"/></svg></div>
    </div>
  </section>

  <!-- Business card, back -->
  <section class="card card--back" aria-label="Business card back">
    <div class="firm">
      <span class="firm__square"></span>
      <span class="firm__name">MARLOW</span>
      <span class="firm__suffix">LAW LLC</span>
    </div>
  </section>

  <!-- Envelope -->
  <section class="envelope" aria-label="Envelope">
    <svg class="shapes" viewBox="0 0 852 424" preserveAspectRatio="none" aria-hidden="true">
      <path class="ink" d="M0 396 H420 Q432 396 440 388 L470 356 Q478 348 490 348 H852 V424 H0 Z"/>
      <path class="amber" d="M0 363 H406 Q415 363 411 369 L405 380 Q401 386 394 386 H0 Z"/>
    </svg>
    <div class="firm">
      <span class="firm__square"></span>
      <span class="firm__name">MARLOW</span>
      <span class="firm__suffix">LAW LLC</span>
    </div>
    <div class="contact" style="top:218px">
      <svg viewBox="0 0 9 12"><rect x="1" y="0.7" width="7" height="10.6" rx="1.2" fill="none" stroke="currentColor" stroke-width="1.3"/><rect x="3.5" y="9" width="2" height="1" fill="currentColor"/></svg>
      <span>+39 000 5550142</span>
    </div>
    <div class="contact" style="top:252px">
      <svg viewBox="0 0 10 8"><rect width="10" height="8" rx="1" fill="currentColor"/><path d="M1 1.5 L5 4.5 L9 1.5" fill="none" stroke="#fff" stroke-width="1"/></svg>
      <span>office@marlowlaw.com</span>
    </div>
    <span class="web">www.marlowlaw.com</span>
  </section>

</div>
</body>
</html>
```